I have a website called Quellmark Estates (quellmarkestates.com) that I would like to have redesigned. Most of the content is already created, but I need a new design. You can also see my other website at dovanholdings.com. I am open to a new logo or modifying the current logo if you have a good idea. Please feel free to use other images for the home page (and maybe some other locations) if you feel they provide a better look and feel to the website. I prefer a modern look.

Important: You do not have to use the images I've provided for the home page. Feel free to find your own stock photos. You don't have to pay for them unless I select your design.

1) Please use wix.com to make your changes so that I can edit it later.
2) I will need all the graphics files to be saved so I can dowload it for later.
3) I will be adding more content to the site later.
4) This site will likely be transferred over to dovanholdings.com so if you make a logo please make one for Quellmark Estates and one for Dovan Holdings.
5) You can use other images that you feel would help the look and feel of the website.

Real Estate

```html
<!DOCTYPE html>
<html lang="en">
<head>
<meta charset="utf-8">
<title>Quellmark Estates</title>
<link rel="stylesheet" href="https://fonts.googleapis.com/css2?family=Lato:wght@400;700;900&family=Montserrat:wght@600;700;800&family=Oswald:wght@500&family=Roboto:wght@400;500;700&display=swap">
<style>
:root{
  --blue:#1762e6;
  --navy:#0b1b42;
  --navy-2:#0a1736;
  --text:#333;
  --line:#d6d9e0;
  --white:#fff;
  --partner-bg:#eceef1;
}
*{box-sizing:border-box;margin:0;padding:0}
html,body{width:1200px;height:4396px;overflow:hidden}
body{position:relative;font-family:'Lato',sans-serif;color:var(--text);background:var(--white)}
.abs{position:absolute}
.btn{position:absolute;display:flex;align-items:center;justify-content:center;background:var(--blue);color:var(--white);font:700 16px 'Lato',sans-serif;letter-spacing:.2px}

/* top bar */
.topbar{left:0;top:0;width:1200px;height:55px;background:var(--blue)}
.social{top:16px;width:22px;height:22px;border-radius:50%;background:var(--white)}
.topbar .tlink{top:17px;color:var(--white);font:400 15px 'Lato',sans-serif;display:flex;align-items:center;gap:8px;white-space:nowrap}
.topbar svg{fill:var(--white)}

/* nav */
.nav{left:0;top:55px;width:1200px;height:66px;background:var(--white)}
.brand{left:102px;top:16px;display:flex;align-items:center;gap:12px;font:700 21px 'Lato',sans-serif;color:var(--blue)}
.brand-mark{width:30px;height:30px;background:var(--navy)}
.menu{top:22px;font:700 16px 'Lato',sans-serif;color:#333}
.menu.active{color:#111;font-weight:900}
.nav .btn{left:961px;top:13px;width:133px;height:38px;font-size:15px}

/* hero */
.hero{left:0;top:121px;width:1200px;height:674px;background:linear-gradient(180deg,#4a4f66 0%,#6f6670 30%,#8c6a52 48%,#3b3a44 70%,#22242c 100%)}
.hero .welcome{left:154px;top:175px;font:400 29px 'Lato',sans-serif;color:var(--white)}
.hero h1{position:absolute;left:152px;top:213px;font:700 58px 'Lato',sans-serif;color:var(--white);white-space:nowrap}
.hero .sub{left:154px;top:303px;font:400 26px/1.3 'Lato',sans-serif;color:var(--white);width:420px}
.hero .btn{left:148px;top:396px;width:175px;height:56px}
.form{left:671px;top:103px;width:427px;height:474px;background:var(--blue);border:5px solid #a9adb7;border-radius:10px}
.form h2{position:absolute;left:0;width:100%;top:40px;text-align:center;font:700 25px 'Montserrat',sans-serif;color:var(--white)}
.form .rule{left:183px;top:84px;width:52px;height:3px;background:var(--white)}
.field{left:37px;width:340px;height:44px;background:var(--white);border-radius:8px;font:400 15px 'Lato',sans-serif;color:#333;padding:13px 38px}
.form .submit{left:142px;top:379px;width:133px;height:36px;background:var(--navy-2);font-size:14px}

/* about */
.about-ring{left:85px;top:879px;width:400px;height:400px;border-radius:50%;background:var(--blue)}
.about-photo{left:110px;top:896px;width:372px;height:372px;border-radius:50%;background:linear-gradient(160deg,#c9d7ea 0%,#8a7b6c 45%,#4a4038 100%);border:6px solid var(--white)}
.about-dot{left:379px;top:1219px;width:88px;height:88px;border-radius:50%;background:var(--navy-2)}
.h-section{font:700 37px 'Montserrat',sans-serif;color:var(--blue);letter-spacing:.5px}
.about h2{position:absolute;left:570px;top:898px}
.about p{position:absolute;left:570px;top:966px;width:490px;font:400 16px/30px 'Lato',sans-serif;color:#222;text-align:justify}
.about .btn{left:570px;top:1268px;width:167px;height:57px}

/* stats */
.stats{left:0;top:1425px;width:1200px;height:311px;background:var(--blue)}
.stat{position:absolute;top:46px;width:154px;height:152px;background:var(--navy);border:3px solid #0a2f7a;border-radius:6px;box-shadow:0 0 0 2px #3b7bf0}
.stat svg{position:absolute;left:53px;top:26px;fill:var(--white)}
.stat b{position:absolute;left:0;top:84px;width:100%;text-align:center;font:500 30px 'Oswald',sans-serif;color:var(--white);white-space:nowrap;letter-spacing:-.3px}
.stat i{position:absolute;left:43px;top:128px;width:62px;height:2px;background:var(--blue)}
.stat-label{position:absolute;top:222px;width:240px;text-align:center;font:700 18px/26px 'Lato',sans-serif;color:var(--white)}

/* strategy */
.strategy h2{position:absolute;left:0;width:1200px;top:1810px;text-align:center}
.strategy p{position:absolute;left:218px;top:1878px;width:764px;text-align:center;font:400 16px/30px 'Lato',sans-serif;color:#222}
.strategy .btn{left:515px;top:2065px;width:169px;height:58px}
.card{position:absolute;background:var(--white);border:1px solid var(--line);border-radius:4px;padding:0 22px;font:400 15px 'Roboto',sans-serif;color:#333}
.card.lift{box-shadow:0 6px 18px rgba(0,0,0,.14);border-color:#e6e6e6}
.card svg.ico{position:absolute;left:22px;top:22px}
.card h3{font:700 17px/24px 'Roboto',sans-serif;color:#222;margin:0 0 10px}
.card h4{font:500 16px 'Roboto',sans-serif;color:#222;margin:22px 0 10px 22px}
.card ul{list-style:none}
.card li{position:relative;line-height:20px;margin-bottom:17px}
.card .bul li{padding-left:22px}
.card .bul li::before{content:"";position:absolute;left:2px;top:6px;width:10px;height:7px;background:#3a78d8;border-radius:50%/60%}

/* projects */
.projects{left:0;top:2817px;width:1200px;height:805px;background:linear-gradient(180deg,#1d66e8,#1359da)}
.projects h2{position:absolute;left:0;width:1200px;top:86px;text-align:center;font:700 37px 'Montserrat',sans-serif;color:var(--white)}
.proj{position:absolute;top:204px;width:226px;height:431px}
.proj .ph{position:absolute;left:0;top:0;width:226px;height:240px}
.proj .info{position:absolute;left:5px;top:239px;width:216px;height:192px;background:var(--white);border-radius:4px;padding:18px 16px;font:400 13.5px/22px 'Roboto',sans-serif;color:#333}
.proj h3{position:relative;padding-left:30px;font:500 15.5px/22px 'Roboto',sans-serif;color:#222;margin-bottom:12px}
.proj h3 svg{position:absolute;left:0;top:2px;fill:var(--navy)}
.proj .type{margin-top:12px}
.projects .btn{left:493px;top:687px;width:169px;height:59px;background:var(--white);color:var(--blue);border-radius:3px}

/* partners */
.partners h2{position:absolute;left:0;width:1200px;top:3699px;text-align:center;font:700 37px 'Montserrat',sans-serif;color:var(--blue)}
.partner-strip{left:160px;top:3774px;width:845px;height:104px;background:var(--partner-bg)}
.badge{position:absolute;top:36px;height:32px;background:#9aa0a8;border-radius:4px}

/* footer */
.footer{left:0;top:3895px;width:1200px;height:501px;background:var(--navy-2);color:var(--white)}
.footer h2{position:absolute;left:108px;top:84px;font:700 33px 'Montserrat',sans-serif;letter-spacing:.5px}
.footer .lead{left:110px;top:138px;width:520px;font:400 16px/31px 'Roboto',sans-serif}
.footer .callback{left:860px;top:103px;width:229px;height:63px;border:2px solid var(--white);display:flex;align-items:center;justify-content:center;font:700 16px 'Roboto',sans-serif}
.footer .hr{left:108px;width:981px;height:1px;background:#2c3a5e}
.footer .vr{top:253px;width:1px;height:172px;background:#2c3a5e}
.fcol{position:absolute;top:288px}
.fcol .circ{position:absolute;left:0;top:0;width:48px;height:48px;border-radius:50%;background:var(--blue);display:flex;align-items:center;justify-content:center}
.fcol .circ svg{fill:var(--white)}
.fcol h4{position:absolute;left:65px;top:14px;white-space:nowrap;font:700 16px 'Roboto',sans-serif}
.fcol p{position:absolute;left:65px;top:46px;white-space:nowrap;font:400 15px/32px 'Roboto',sans-serif}
.footer .copy{left:108px;top:469px;font:400 14px 'Roboto',sans-serif}
.footer .legal{right:111px;top:469px;font:400 14px 'Roboto',sans-serif}
</style>
</head>
<body>

<div class="abs topbar">
  <span class="abs social" style="left:117px"></span>
  <span class="abs social" style="left:148px"></span>
  <span class="abs social" style="left:179px"></span>
  <span class="tlink abs" style="left:697px"><svg width="20" height="20" viewBox="0 0 20 20"><circle cx="10" cy="10" r="9"/><text x="10" y="14.5" text-anchor="middle" font-size="12" font-weight="700" fill="#1762e6" font-family="Lato,sans-serif">$</text></svg>Pricing</span>
  <span class="tlink abs" style="left:800px"><svg width="22" height="20" viewBox="0 0 22 20"><path d="M11 2a8 8 0 0 0-8 8v5h4v-6H5a6 6 0 0 1 12 0h-2v6h4v-5a8 8 0 0 0-8-8z"/></svg>Call Us: (555) 314-2760</span>
  <span class="tlink abs" style="left:1024px"><svg width="22" height="22" viewBox="0 0 22 22"><circle cx="11" cy="11" r="10"/><circle cx="11" cy="8.5" r="3.6" fill="#1762e6"/><path d="M4.5 17a8 8 0 0 1 13 0" fill="#1762e6"/></svg>Login</span>
</div>

<div class="abs nav">
  <div class="abs brand"><span class="brand-mark"></span>Quellmark Estates</div>
  <span class="abs menu active" style="left:536px">HOME</span>
  <span class="abs menu" style="left:625px">ABOUT</span>
  <span class="abs menu" style="left:717px">STRATEGY</span>
  <span class="abs menu" style="left:836px">PROJECTS</span>
  <span class="btn">CONTACT US</span>
</div>

<section class="abs hero">
  <div class="abs" role="img" aria-label="City skyline at sunset" style="inset:0"></div>
  <div class="abs welcome">Welcome To</div>
  <h1>Quellmark Estates</h1>
  <div class="abs sub">Private Commercial Real Estate Investment and Development Firm</div>
  <span class="btn">LEARN MORE</span>
  <div class="abs form">
    <h2>Get In Touch</h2>
    <span class="abs rule"></span>
    <div class="abs field" style="top:129px">Name</div>
    <div class="abs field" style="top:189px">Phone</div>
    <div class="abs field" style="top:249px">Email ID</div>
    <div class="abs field" style="top:308px">Address</div>
    <span class="btn submit">SUBMIT</span>
  </div>
</section>

<section class="about">
  <div class="abs about-ring"></div>
  <div class="abs about-photo" role="img" aria-label="Modern brick and glass office building"></div>
  <div class="abs about-dot"></div>
  <h2 class="h-section">ABOUT US</h2>
  <p>Dovan Holdings is a private real estate firm that specializes in the procurement, development, management, and disposition of various commercial real estate asset types including multifamily, industrial, single-family, hospitality, self-storage, and flex. The firm effectuates its strategy by utilizing long-standing relationships to ascertain acquisition and development opportunities within a specific target market. Dovan Holdings is currently focused on acquisition and development opportunities in the southern portion of the United States.</p>
  <span class="btn">LEARN MORE</span>
</section>

<section class="abs stats">
  <div class="stat" style="left:114px"><svg width="42" height="42" viewBox="0 0 42 42"><path d="M4 40V6h16v34zM22 40V16h16v24z"/><g fill="#0b1b42"><rect x="8" y="10" width="3" height="4"/><rect x="13" y="10" width="3" height="4"/><rect x="8" y="18" width="3" height="4"/><rect x="13" y="18" width="3" height="4"/><rect x="26" y="22" width="3" height="4"/><rect x="31" y="22" width="3" height="4"/></g></svg><b>2017</b><i></i></div>
  <div class="stat-label" style="left:64px">YEAR ESTABLISHED</div>
  <div class="stat" style="left:391px"><svg width="42" height="42" viewBox="0 0 42 42"><path d="M21 3L2 19h5v20h28V19h5z"/><rect x="17" y="26" width="8" height="13" fill="#0b1b42"/></svg><b>DALLAS, TX</b><i></i></div>
  <div class="stat-label" style="left:349px">HEADQUARTERS</div>
  <div class="stat" style="left:660px"><svg width="42" height="42" viewBox="0 0 42 42"><path d="M21 2L5 8v12c0 10 7 17 16 20 9-3 16-10 16-20V8z"/><path d="M14 21l5 5 10-10" stroke="#0b1b42" stroke-width="3.5" fill="none"/></svg><b>$100MM+</b><i></i></div>
  <div class="stat-label" style="left:617px">ASSETS UNDER<br>MANAGEMENT</div>
  <div class="stat" style="left:932px"><svg width="48" height="42" viewBox="0 0 48 42"><path d="M6 30a18 18 0 0 1 36 0z"/><rect x="2" y="30" width="44" height="6" rx="2"/><rect x="21" y="8" width="6" height="16" fill="#0b1b42"/></svg><b>6</b><i></i></div>
  <div class="stat-label" style="left:889px">CURRENT PROJECTS</div>
</section>

<section class="strategy">
  <h2 class="h-section">STRATEGY</h2>
  <p>Dovan Holdings evaluates opportunities with a two-pronged approach. First, the firm searches for development opportunities which are in growing metropolitan markets and possess a high barrier to entry. Second, the firm actively purses the acquisition of distressed or value-add assets which yield compelling cash-on-cash returns. The diverse background of the firm avails an opportunistic and entrepreneurial evaluation of each transaction.</p>
  <span class="btn">LEARN MORE</span>

  <div class="card" style="left:-15px;top:2207px;width:305px;height:340px;padding-left:26px">
    <svg class="ico" style="left:26px" width="68" height="64" viewBox="0 0 68 64"><path d="M40 2l26 60H30z" fill="#cfe0f7"/><circle cx="24" cy="38" r="16" fill="none" stroke="#2f74d6" stroke-width="3"/><rect x="14" y="34" width="4" height="12" fill="#2f74d6"/><rect x="21" y="28" width="4" height="18" fill="#2f74d6"/><rect x="28" y="24" width="4" height="22" fill="#2f74d6"/></svg>
    <div style="margin-top:118px"><h3>Investment Focus</h3>
    <ul style="margin-top:8px"><li>Ground-up Development</li><li>Value-Add Acquisition</li><li>Equity Financing</li><li>Debt Financing</li></ul></div>
  </div>

  <div class="card lift" style="left:321px;top:2181px;width:305px;height:547px">
    <svg class="ico" width="68" height="64" viewBox="0 0 68 64"><path d="M40 2l26 60H30z" fill="#cfe0f7"/><circle cx="26" cy="34" r="14" fill="none" stroke="#2f74d6" stroke-width="3" stroke-dasharray="5 3"/><circle cx="26" cy="34" r="7" fill="#2f74d6"/></svg>
    <div style="margin-top:110px"><h3>Development</h3>
    <h4 style="margin-top:12px">Site Selection:</h4>
    <ul class="bul"><li>Undeveloped Land</li><li>Entitled Land</li><li>Urban Redevelopment</li></ul>
    <h4>Multiple Construction Types:</h4>
    <ul class="bul"><li>Single Story Garden</li><li>Wrap Construction</li><li>Podium Construction</li><li>Tiltwall</li></ul></div>
  </div>

  <div class="card" style="left:657px;top:2207px;width:306px;height:369px">
    <svg class="ico" width="68" height="64" viewBox="0 0 68 64"><path d="M40 2l26 60H30z" fill="#cfe0f7"/><circle cx="24" cy="38" r="16" fill="none" stroke="#2f74d6" stroke-width="3"/><rect x="14" y="34" width="4" height="12" fill="#2f74d6"/><rect x="21" y="28" width="4" height="18" fill="#2f74d6"/><rect x="28" y="24" width="4" height="22" fill="#2f74d6"/></svg>
    <div style="margin-top:118px"><h3>Acquisitions: Distressed/<br>Value-Add</h3>
    <ul class="bul" style="margin-top:18px"><li style="line-height:17px;text-align:justify">Assets which yeild cash-on-cash returns as well as rent growth and exit upside.</li><li>Major Metropolitan Areas</li><li style="line-height:17px;text-align:justify;padding-right:14px">Asset Value between $10 - $75mm</li></ul></div>
  </div>

  <div class="card" style="left:992px;top:2207px;width:306px;height:383px">
    <svg class="ico" width="68" height="64" viewBox="0 0 68 64"><path d="M40 2l26 60H30z" fill="#cfe0f7"/><path d="M12 14h34l-8 22h-18z" fill="none" stroke="#2f74d6" stroke-width="3"/><rect x="22" y="38" width="14" height="10" fill="#2f74d6"/></svg>
    <div style="margin-top:118px"><h3>Product Types</h3>
    <ul class="bul" style="margin-top:8px"><li>YMultifamily</li><li>Industrial</li><li>SFR Communities</li><li>Self-Storage</li><li>Hospitality</li><li>Retail</li></ul></div>
  </div>
</section>

<section class="abs projects">
  <div class="abs" role="img" aria-label="Faded photo of an apartment community entrance" style="left:300px;top:60px;width:600px;height:300px;background:radial-gradient(ellipse at center,rgba(255,255,255,.08),rgba(255,255,255,0) 70%)"></div>
  <h2>PROJECTS</h2>
  <div class="proj" style="left:104px">
    <div class="ph" role="img" aria-label="Multi-story residential building with trees" style="background:linear-gradient(180deg,#c9d4df,#9c8a72 60%,#5d6b48)"></div>
    <div class="info"><h3><svg width="16" height="20" viewBox="0 0 16 20"><path d="M8 0a8 8 0 0 0-8 8c0 6 8 12 8 12s8-6 8-12a8 8 0 0 0-8-8zm0 11a3 3 0 1 1 0-6 3 3 0 0 1 0 6z"/></svg>Crestline Harbor Residences</h3>Class A Multifamily - 176 Units - 4 Story - 159,280 SF - 3 Acres<div class="type">Ground-up Development</div></div>
  </div>
  <div class="proj" style="left:353px">
    <div class="ph" role="img" aria-label="Apartment complex rendering with courtyard" style="background:linear-gradient(180deg,#dfe7ef,#7d7a78 55%,#5f8a48)"></div>
    <div class="info"><h3><svg width="16" height="20" viewBox="0 0 16 20"><path d="M8 0a8 8 0 0 0-8 8c0 6 8 12 8 12s8-6 8-12a8 8 0 0 0-8-8zm0 11a3 3 0 1 1 0-6 3 3 0 0 1 0 6z"/></svg>Lakeview at Alder Creek</h3>Class A Multifamily - 373 Units - 3 Story - 345,297 SF - 24.31 Acres<div class="type">Ground-up Development</div></div>
  </div>
  <div class="proj" style="left:604px">
    <div class="ph" role="img" aria-label="White industrial warehouse building" style="background:linear-gradient(180deg,#2a6ee0,#e8eaed 45%,#9a9c9e)"></div>
    <div class="info"><h3><svg width="16" height="20" viewBox="0 0 16 20"><path d="M8 0a8 8 0 0 0-8 8c0 6 8 12 8 12s8-6 8-12a8 8 0 0 0-8-8zm0 11a3 3 0 1 1 0-6 3 3 0 0 1 0 6z"/></svg>Harlow Industrial</h3>Class A Industrial - 170,000 SF - 10.10 Acres<div class="type" style="margin-top:16px">Ground-up Development</div></div>
  </div>
  <div class="proj" style="left:854px">
    <div class="ph" role="img" aria-label="Modern townhomes with wood and stucco facade" style="background:linear-gradient(180deg,#b9c8d8,#8b7662 50%,#d6d0c8)"></div>
    <div class="info"><h3><svg width="16" height="20" viewBox="0 0 16 20"><path d="M8 0a8 8 0 0 0-8 8c0 6 8 12 8 12s8-6 8-12a8 8 0 0 0-8-8zm0 11a3 3 0 1 1 0-6 3 3 0 0 1 0 6z"/></svg>Fenwick Homes</h3>Class A Multifamily - 23 Units - 3 Story - 42,000 SF - .78 Acres<div class="type" style="margin-top:16px">Ground-up Development</div></div>
  </div>
  <span class="btn">VIEW ALL</span>
</section>

<section class="partners">
  <h2>CORPORATE PARTNERS</h2>
  <div class="abs partner-strip">
    <span class="badge" style="left:22px;width:102px;background:#2a2a2a"></span>
    <span class="badge" style="left:193px;width:103px"></span>
    <span class="badge" style="left:370px;width:104px;background:#3a3a3a"></span>
    <span class="badge" style="left:534px;width:115px;background:#9a1e5e"></span>
    <span class="badge" style="left:710px;width:108px"></span>
  </div>
</section>

<footer class="abs footer">
  <h2>WE ARE HERE TO HELP YOU</h2>
  <div class="abs lead">To apply for a job with Dovan Holdings, please send a cover letter together with your C.V. to: info@dovanholdings.com</div>
  <div class="abs callback">REQUEST A CALL BACK</div>
  <span class="abs hr" style="top:253px"></span>
  <span class="abs vr" style="left:410px"></span>
  <span class="abs vr" style="left:751px"></span>
  <div class="fcol" style="left:107px">
    <span class="circ"><svg width="18" height="24" viewBox="0 0 16 20"><path d="M8 0a8 8 0 0 0-8 8c0 6 8 12 8 12s8-6 8-12a8 8 0 0 0-8-8zm0 11a3 3 0 1 1 0-6 3 3 0 0 1 0 6z"/></svg></span>
    <h4>HEAD QUARTERS</h4>
    <p>480 Larkspur Ave. 7th Floor<br>Dallas, Texas 75201</p>
  </div>
  <div class="fcol" style="left:450px">
    <span class="circ"><svg width="22" height="22" viewBox="0 0 24 24"><path d="M6.6 10.8a15 15 0 0 0 6.6 6.6l2.2-2.2a1 1 0 0 1 1-.25 11.4 11.4 0 0 0 3.6.57 1 1 0 0 1 1 1V20a1 1 0 0 1-1 1A17 17 0 0 1 3 4a1 1 0 0 1 1-1h3.5a1 1 0 0 1 1 1c0 1.250.2 2.450.57 3.57a1 1 0 0 1-.25 1z"/></svg></span>
    <h4>PHONE NO</h4>
    <p>(555) 314-2760</p>
  </div>
  <div class="fcol" style="left:823px">
    <span class="circ"><svg width="24" height="18" viewBox="0 0 24 18"><path d="M0 0h24v18H0z"/><path d="M1 1l11 9 11-9" stroke="#1762e6" stroke-width="2" fill="none"/></svg></span>
    <h4>MAIL</h4>
    <p>info@dovanholdings.com</p>
  </div>
  <span class="abs hr" style="top:451px"></span>
  <div class="abs copy">Copyright 2022 Quellmark Estates | All Rights Reserved</div>
  <div class="abs legal">Privacy &amp; Cookie Policy &nbsp;|&nbsp; Terms &amp; Conditions</div>
</footer>

</body>
</html>
```